eCommerce Website Design for Electronic Kits

The company is called Vantrelle. We develop electronic kits, parts & tutorials for hobbyists and engineers. I want something bigger than myself. I can develop and code something, but I want it to be more than I can imagine, so I am here. So, if you feel you have something unique but outside my direction, go for it! I am leaning toward a darker, modern, clean look with a "retro feel," maybe purples, bright reds/pinks, or neon. Our competition is https://www.korbimelt.example and https://www.duvessland.example

Target Market(s)

Hobyists & Engineers (electronics and 3d printing)

Industry/Entity Type

Electronic parts, kits, PCBs, tutorials

Number of Pages Required

4 page

Font styles to use
Sans Serif

Colors

Designer to choose colors to be used in the design.

Requirements
Must have
• Landing / Main Page, Shopping Cart, Item Detail, Blog Post

```html
<!DOCTYPE html>
<html lang="en">
<head>
<meta charset="utf-8">
<title>Vantrelle — Electronic Kits</title>
<link href="https://fonts.googleapis.com/css2?family=Questrial&family=Roboto:wght@400;500;700&display=swap" rel="stylesheet">
<style>
:root{
  --bg:#000;
  --panel:#1a0a1a;
  --accent:#e8291c;
  --white:#fff;
  --field:#2e2a33;
}
*{margin:0;padding:0;box-sizing:border-box}
html,body{width:1200px;height:3363px;overflow:hidden;background:var(--bg);color:var(--white);font-family:Roboto,Arial,sans-serif}
.page{position:relative;width:1200px;height:3363px;overflow:hidden;
  background:linear-gradient(180deg,#000 0,#000 1700px,#0c0714 1900px,#120a1c 2400px,#0d0812 2900px,#140a1a 3363px)}
.abs{position:absolute}
.display{font-family:Questrial,Arial,sans-serif;letter-spacing:-.07em;font-weight:400}

/* header */
.brand{left:98px;top:18px;width:140px;text-align:center}
.brand .mark{width:50px;height:50px;border:3px solid var(--white);margin:0 auto 10px}
.brand .name{font-family:Questrial,sans-serif;font-size:30px;letter-spacing:-.02em}
.search{left:770px;top:16px;width:216px;height:43px;border:1px solid #bbb;display:flex;align-items:center;justify-content:space-between;padding:0 14px;font-size:16px;font-weight:500}
.currency{left:1009px;top:16px;width:92px;height:43px;border:1px solid #bbb;display:flex;align-items:center;justify-content:space-between;padding:0 14px;font-size:16px;font-weight:500}
.nav{left:468px;top:97px;display:flex;font-family:Questrial,sans-serif;font-size:17px;letter-spacing:-.06em}
.nav a{color:var(--white);text-decoration:none;margin-right:37px}
.cart{left:1038px;top:85px;width:42px;height:42px;border-radius:50%;background:var(--accent);display:flex;align-items:center;justify-content:center}
.cart-count{left:1075px;top:72px;font-size:15px;font-weight:500}

/* hero */
.hero{left:0;top:154px;width:1200px;height:599px;
  background:
    radial-gradient(circle at 600px 180px,rgba(190,70,80,.95) 0,rgba(120,40,90,.8) 110px,rgba(60,20,70,0) 200px),
    radial-gradient(circle at 160px 105px,rgba(140,40,40,.55) 0,rgba(140,40,40,0) 45px),
    radial-gradient(ellipse 900px 120px at 600px 330px,rgba(230,60,150,.45),rgba(230,60,150,0)),
    linear-gradient(180deg,#0a0b28 0,#161238 30%,#2c1550 48%,#54206a 55%,#2a2a78 63%,#1a3a7a 78%,#1a5070 92%,#0e3048 100%)}
.hero-name{left:0;top:310px;width:1200px;text-align:center;font-size:56px;letter-spacing:-.04em}
.hero-title{left:0;top:520px;width:1200px;text-align:center;font-size:62px}
.dots{left:570px;top:681px;display:flex;gap:10px}
.dots span{width:13px;height:13px;border-radius:50%;background:#888}
.dots span.on{background:var(--white)}

/* tabs */
.tabs{left:98px;top:890px;display:flex;align-items:center;font-size:17px}
.tab{margin-right:40px}
.tab.active{background:var(--accent);height:45px;width:121px;display:flex;align-items:center;justify-content:center;margin-right:36px}
.all-cats{left:900px;top:900px;width:201px;text-align:right;color:var(--accent);text-decoration:underline;font-size:17px}

/* products */
.card{top:997px;width:231px;text-align:center}
.card .photo{height:214px;border-radius:3px}
.card .title{margin-top:18px;font-size:22px}
.card .desc{margin-top:12px;font-size:15px}
.card .price{margin-top:14px;font-size:19px;color:var(--accent)}
.arrow{width:20px;height:32px}

/* shipping */
.shipping{left:98px;top:1452px;width:1003px;height:155px;border:1.5px solid var(--accent);border-radius:12px;background:var(--panel)}
.shipping h2{position:absolute;left:0;top:38px;width:100%;text-align:center;font-size:34px;font-weight:400}
.shipping p{position:absolute;left:0;top:100px;width:100%;text-align:center;font-size:15px}
.truck{top:40px}

/* topics */
.section-title{left:0;width:1200px;text-align:center;font-size:37px}
.topic{top:1876px;width:211px;text-align:center}
.topic .hex{width:211px;height:242px;clip-path:polygon(50% 0,100% 25%,100% 75%,50% 100%,0 75%,0 25%)}
.topic .label{margin-top:24px;font-size:18px;font-weight:500}

/* blog */
.blog{left:97px;top:2416px;width:1004px;height:380px;border:2px solid var(--accent);display:flex}
.post{position:relative;width:50%;height:100%}
.post + .post{border-left:2px solid var(--accent)}
.post .caption{position:absolute;left:0;bottom:0;width:100%;height:122px;background:rgba(0,0,0,.55);padding:38px 34px 0}
.post h3{font-size:23px;font-weight:400}
.post p{margin-top:14px;font-size:15px}
.post .go{position:absolute;right:30px;top:52px}

/* footer */
.foot-brand{left:74px;top:2972px;width:170px;text-align:center}
.foot-brand .mark{width:74px;height:74px;border:4px solid var(--white);margin:0 auto 20px}
.foot-brand .name{font-family:Questrial,sans-serif;font-size:38px;letter-spacing:-.02em}
.social{left:70px;top:3177px;display:flex;gap:18px}
.social span{width:32px;height:32px;border-radius:50%;background:var(--accent);border:2px solid var(--white)}
.col-title{font-size:20px;font-weight:700}
.col-title::after{content:"";display:block;width:48px;height:3px;background:var(--white);margin-top:12px}
.links{list-style:none;font-size:15px}
.links li{height:31px}
.contact{list-style:none;font-size:15px}
.contact li{display:flex;align-items:center;gap:12px;height:60px}
.contact .ic{width:36px;height:36px;border-radius:50%;background:var(--field);display:flex;align-items:center;justify-content:center}
.email{left:885px;top:3106px;width:251px;height:42px;display:flex}
.email .field{flex:1;background:var(--white);color:#333;font-size:12px;padding:15px 22px}
.email .send{width:42px;background:var(--accent);display:flex;align-items:center;justify-content:center}
.divider{left:47px;top:3295px;width:1106px;height:1px;background:#aaa}
.copyright{left:0;top:3321px;width:1200px;text-align:center;font-size:15px}
</style>
</head>
<body>
<div class="page">

  <!-- header -->
  <div class="abs brand"><div class="mark"></div><div class="name">Vantrelle</div></div>
  <div class="abs search">Search
    <svg width="18" height="18" viewBox="0 0 18 18" fill="none" stroke="#fff" stroke-width="2"><circle cx="7.5" cy="7.5" r="6"/><path d="M12 12l5 5"/></svg>
  </div>
  <div class="abs currency">USD
    <svg width="10" height="7" viewBox="0 0 10 7" fill="none" stroke="#fff" stroke-width="1.6"><path d="M1 1l4 4 4-4"/></svg>
  </div>
  <nav class="abs nav"><a>Products</a><a>Gift Ideas</a><a>What's New</a><a>Shop</a><a>Blog</a><a>Contact Us</a></nav>
  <div class="abs cart">
    <svg width="20" height="18" viewBox="0 0 20 18" fill="none" stroke="#fff" stroke-width="1.8"><path d="M1 2h3l2 10h10l2-7H5"/><circle cx="8" cy="15.5" r="1.3"/><circle cx="15" cy="15.5" r="1.3"/></svg>
  </div>
  <div class="abs cart-count">(0)</div>

  <!-- hero -->
  <div class="abs hero" role="img" aria-label="Retro synthwave landscape: neon wireframe mountains and grid floor under a glowing red sun and moon"></div>
  <div class="abs hero-name display">Vantrelle</div>
  <h1 class="abs hero-title display">WELCOME TO VANTRELLE</h1>
  <div class="abs dots"><span></span><span class="on"></span><span></span></div>

  <!-- product tabs -->
  <div class="abs tabs display">
    <span class="tab active">New Products</span>
    <span class="tab">Top Sellers</span>
    <span class="tab">Forgeline Originals</span>
    <span class="tab">On Sale</span>
  </div>
  <a class="abs all-cats display">All product categories</a>

  <svg class="abs arrow" style="left:42px;top:1120px" viewBox="0 0 20 32" fill="none" stroke="#fff" stroke-width="2"><path d="M16 2L3 16l13 14"/></svg>
  <svg class="abs arrow" style="left:1140px;top:1120px" viewBox="0 0 20 32" fill="none" stroke="#fff" stroke-width="2"><path d="M4 2l13 14L4 30"/></svg>

  <div class="abs card" style="left:98px"><div class="photo" role="img" aria-label="Precision tool kit in a black zip case" style="background:radial-gradient(ellipse 70px 36px at 50% 52%,#2a2e38,#6a7080 60%,rgba(255,255,255,0) 100%),#fff"></div><div class="title display">Lorem ipsum dolor</div><div class="desc">Sed ut perspiciatis unde</div><div class="price display">$45.00</div></div>
  <div class="abs card" style="left:355px"><div class="photo" role="img" aria-label="Wi-Fi microcontroller development board" style="background:radial-gradient(ellipse 70px 45px at 50% 52%,#3a3a3a,#8a8070 60%,rgba(255,255,255,0) 100%),#fff"></div><div class="title display">Lorem ipsum dolor</div><div class="desc">Sed ut perspiciatis unde</div><div class="price display">$45.00</div></div>
  <div class="abs card" style="left:613px"><div class="photo" role="img" aria-label="LED dot matrix display module with cable" style="background:radial-gradient(ellipse 95px 26px at 55% 52%,#8a7a60,#c8c0b0 60%,rgba(255,255,255,0) 100%),linear-gradient(180deg,#fff,#e8e8e8)"></div><div class="title display">Lorem ipsum dolor</div><div class="desc">Sed ut perspiciatis unde</div><div class="price display">$45.00</div></div>
  <div class="abs card" style="left:870px"><div class="photo" role="img" aria-label="Soldering iron, solder spool and green circuit board" style="background:radial-gradient(ellipse 50px 40px at 55% 58%,#1f8a3a,#8ac89a 60%,rgba(255,255,255,0) 100%),#fff"></div><div class="title display">Lorem ipsum dolor</div><div class="desc">Sed ut perspiciatis unde</div><div class="price display">$45.00</div></div>

  <!-- shipping banner -->
  <div class="abs shipping">
    <svg class="abs truck" style="left:44px" width="126" height="72" viewBox="0 0 126 72" fill="#fff"><rect x="22" y="6" width="66" height="46" rx="6"/><path d="M90 18h16l14 18v16H90z"/><circle cx="42" cy="58" r="11" stroke="#1a0a1a" stroke-width="4"/><circle cx="98" cy="58" r="11" stroke="#1a0a1a" stroke-width="4"/><rect x="0" y="14" width="16" height="5" rx="2"/><rect x="4" y="28" width="14" height="5" rx="2"/><rect x="0" y="42" width="16" height="5" rx="2"/></svg>
    <h2 class="display">FREE SHIPPING* ON ORDERS OVER $100</h2>
    <p>Lorem ipsum dolor sit amet, consectetur adipiscing elit, sed do eiusmod</p>
    <svg class="abs truck" style="right:44px;transform:scaleX(-1)" width="126" height="72" viewBox="0 0 126 72" fill="#fff"><rect x="22" y="6" width="66" height="46" rx="6"/><path d="M90 18h16l14 18v16H90z"/><circle cx="42" cy="58" r="11" stroke="#1a0a1a" stroke-width="4"/><circle cx="98" cy="58" r="11" stroke="#1a0a1a" stroke-width="4"/><rect x="0" y="14" width="16" height="5" rx="2"/><rect x="4" y="28" width="14" height="5" rx="2"/><rect x="0" y="42" width="16" height="5" rx="2"/></svg>
  </div>

  <!-- topics -->
  <h2 class="abs section-title display" style="top:1785px">LEARN ABOUT POPULAR ELECTRONICS TOPICS</h2>
  <svg class="abs arrow" style="left:42px;top:1990px" viewBox="0 0 20 32" fill="none" stroke="#fff" stroke-width="2"><path d="M16 2L3 16l13 14"/></svg>
  <svg class="abs arrow" style="left:1140px;top:1990px" viewBox="0 0 20 32" fill="none" stroke="#fff" stroke-width="2"><path d="M4 2l13 14L4 30"/></svg>
  <div class="abs topic" style="left:98px"><div class="hex" role="img" aria-label="Robotic arm assembling circuit boards on a production line" style="background:radial-gradient(circle at 50% 30%,#c08a30,rgba(192,138,48,0) 45%),linear-gradient(170deg,#9aa0a8,#6a7a70 55%,#3d6a4a)"></div><div class="label">Lorem ipsum dolor</div></div>
  <div class="abs topic" style="left:362px"><div class="hex" role="img" aria-label="Location pin glowing over a circuit board" style="background:radial-gradient(circle at 50% 45%,#4aa8e8,rgba(74,168,232,0) 30%),linear-gradient(160deg,#3a4a7a,#1a2550 60%,#121d3d)"></div><div class="label">Lorem ipsum dolor</div></div>
  <div class="abs topic" style="left:626px"><div class="hex" role="img" aria-label="Hand touching a glowing RFID chip" style="background:radial-gradient(circle at 68% 48%,#5aa0ff,rgba(90,160,255,0) 40%),linear-gradient(160deg,#1f4aa8,#0c1a5a)"></div><div class="label">Lorem ipsum dolor</div></div>
  <div class="abs topic" style="left:890px"><div class="hex" role="img" aria-label="Wireless signal symbol above a laptop keyboard" style="background:radial-gradient(circle at 55% 48%,#8a7080,rgba(138,112,128,0) 30%),linear-gradient(160deg,#f0ecf0,#c8b8c0 60%,#a89aa6)"></div><div class="label">Lorem ipsum dolor</div></div>

  <!-- blog -->
  <h2 class="abs section-title display" style="top:2332px">LATEST BLOG</h2>
  <div class="abs blog">
    <article class="post" role="img" aria-label="Engineer in hard hat and orange overalls repairing an electric motor" style="background:radial-gradient(ellipse 120px 160px at 35% 45%,#d8501c,rgba(216,80,28,0) 100%),radial-gradient(circle at 40% 8%,#e8c020,rgba(232,192,32,0) 18%),linear-gradient(150deg,#6a6a62,#3a3530 60%,#5a2a1a)">
      <div class="caption"><h3 class="display">LOREM IPSUM DOLOR</h3><p>Sed ut perspiciatis unde omnis iste natus sit voluptatem</p>
        <svg class="go" width="14" height="14" viewBox="0 0 14 14" fill="#fff"><path d="M0 5h8V1l6 6-6 6V9H0z"/></svg></div>
    </article>
    <article class="post" role="img" aria-label="Technician assembling a robot kit on a workbench in front of monitors" style="background:radial-gradient(ellipse 160px 140px at 85% 40%,#b09080,rgba(176,144,128,0) 100%),linear-gradient(150deg,#4a4a48,#1e1c1a 45%,#5a5048)">
      <div class="caption"><h3 class="display">LOREM IPSUM DOLOR</h3><p>Sed ut perspiciatis unde omnis iste natus sit voluptatem</p>
        <svg class="go" width="14" height="14" viewBox="0 0 14 14" fill="#fff"><path d="M0 5h8V1l6 6-6 6V9H0z"/></svg></div>
    </article>
  </div>

  <!-- footer -->
  <div class="abs foot-brand"><div class="mark"></div><div class="name">Vantrelle</div></div>
  <div class="abs social" aria-label="Social links"><span></span><span></span><span></span><span></span></div>

  <div class="abs" style="left:364px;top:3002px">
    <div class="col-title">QUICK LINKS</div>
    <ul class="links" style="margin-top:18px"><li>Home</li><li>About Us</li><li>Services</li><li>Blog</li><li>Contact Us</li></ul>
  </div>

  <div class="abs" style="left:572px;top:3002px">
    <div class="col-title">CONTACT US</div>
    <ul class="contact" style="margin-top:6px">
      <li><span class="ic"><svg width="12" height="16" viewBox="0 0 12 16" fill="#fff"><path d="M6 0a6 6 0 0 0-6 6c0 4.5 6 10 6 10s6-5.5 6-10a6 6 0 0 0-6-6zm0 8.5A2.5 2.5 0 1 1 6 3.5a2.5 2.5 0 0 1 0 5z"/></svg></span>Company Name,United State.</li>
      <li><span class="ic"><svg width="16" height="12" viewBox="0 0 16 12" fill="#fff"><path d="M0 0h16v2L8 7 0 2zM0 4l8 5 8-5v8H0z"/></svg></span>info@companyname.in</li>
      <li><span class="ic"><svg width="14" height="14" viewBox="0 0 14 14" fill="#fff"><path d="M3 0l3 3-2 2a9 9 0 0 0 5 5l2-2 3 3-2 3C6 14 0 8 0 2z"/></svg></span>+1888 8888 8888</li>
    </ul>
  </div>

  <div class="abs" style="left:883px;top:3002px">
    <div class="col-title">GET IN TOUCH</div>
    <p style="margin-top:26px;font-size:15px">Lorem ipsum dolor sit amet</p>
  </div>
  <div class="abs email"><div class="field">EMAIL ADDRESS</div>
    <div class="send"><svg width="16" height="16" viewBox="0 0 16 16" fill="#fff"><path d="M16 0L0 7l6 2 2 7z"/></svg></div>
  </div>

  <div class="abs divider"></div>
  <p class="abs copyright">Copyrights@2024.Vantrelle.All Rights Reserved</p>
</div>
</body>
</html>
```